Graphic Design Project

Hi Designers
New Label for New Rum .
The label we would like is it to be modern and smart looking, simple and eye catching. Ingenuity is required and a great open mind to creating this label. Type of rum -Rich flavour with a smooth rounded character. It has robust fruity flavours of molasses, honey and chocolate and is not as sweet as other rums, giving it a strong dark rum taste for the "real rum drinker. If you google Iron Tide Rum thats the type of bottle using .
Name is : Marrow Crest
Size:1l
Alcohol :37.5% Imported Dark Rum
Final designer will be paid extra for posters and t shirt designs. email is devran@tolvik.co.nz
Target Market(s)
Rum Drinkers .
Industry/Entity Type
Graphic Design

```html
<!DOCTYPE html>
<html lang="en">
<head>
<meta charset="utf-8">
<title>Marrow Crest Dark Rum Label</title>
<link rel="stylesheet" href="https://fonts.googleapis.com/css2?family=Marcellus&family=Tenor+Sans&display=swap">
<style>
  :root {
    --page: #ffffff;
    --label: #000000;
    --gold: #c9a24a;
    --gold-light: #e8cf8a;
    --gold-dark: #7a5a1e;
    --ink: #ffffff;
  }
  html, body {
    margin: 0;
    padding: 0;
    width: 924px;
    height: 1200px;
    overflow: hidden;
    background: var(--page);
  }
  .canvas {
    position: relative;
    width: 924px;
    height: 1200px;
  }
  .label {
    position: absolute;
    left: 148px;
    top: 60px;
    width: 628px;
    height: 1080px;
    background: var(--label);
    color: var(--ink);
    font-family: "Tenor Sans", "Optima", sans-serif;
  }
  .ship-art {
    position: absolute;
    left: 44px;
    top: 38px;
    width: 561px;
    height: 546px;
  }
  .brand-name {
    position: absolute;
    left: 178px;
    top: 585px;
    margin: 0;
    font-family: "Marcellus", "Optima", serif;
    font-weight: 400;
    font-size: 60px;
    line-height: 1;
    color: var(--gold);
    white-space: nowrap;
  }
  .origin {
    position: absolute;
    left: 374px;
    top: 651px;
    font-size: 22px;
    line-height: 1;
  }
  .rum-type {
    position: absolute;
    left: 292px;
    top: 672px;
    font-size: 46px;
    line-height: 1;
  }
  .tasting-notes {
    position: absolute;
    left: 160px;
    width: 320px;
    top: 760px;
    margin: 0;
    text-align: center;
    font-size: 23px;
    line-height: 31px;
  }
  .strength {
    position: absolute;
    left: 52px;
    top: 925px;
    font-size: 42px;
    line-height: 1;
  }
  .strength .unit {
    display: block;
    font-size: 29px;
    margin-top: 6px;
  }
  .volume {
    position: absolute;
    left: 508px;
    top: 928px;
    font-size: 42px;
    line-height: 1;
  }
</style>
</head>
<body>
  <main class="canvas">
    <section class="label">
      <svg class="ship-art" role="img" aria-label="Gold illustration of a sailing galleon with full sails and pennants" viewBox="0 0 561 546">
        <defs>
          <radialGradient id="ship-glow" cx="50%" cy="50%" r="55%">
            <stop offset="0%" stop-color="#e8cf8a"/>
            <stop offset="55%" stop-color="#b8923f"/>
            <stop offset="100%" stop-color="#000000"/>
          </radialGradient>
        </defs>
        <ellipse cx="280" cy="280" rx="280" ry="260" fill="url(#ship-glow)"/>
      </svg>
      <h1 class="brand-name">Marrow Crest</h1>
      <span class="origin">Imported</span>
      <span class="rum-type">Dark Rum</span>
      <p class="tasting-notes">Fruity flavours of Molasses<br>Honey &amp; Chocolate</p>
      <div class="strength">37.5%<span class="unit">Alc./Vol.</span></div>
      <div class="volume">1L.</div>
    </section>
  </main>
</body>
</html>
```